Redesign PixelHarbor's Designer Account Home Page

Are a web designer? New to PixelHarbor? This contest is for you!

We want you to redesign PixelHarbor's designer account home page. We're looking for bold and innovative ideas to make this page a useful and fun experience for you and your fellow designers.

Only new registrants this month are eligible to enter this contest and win prizes.

Your task:
* We want you to put your web design skills to the test and re-design the My Account home page ("Overview") on PixelHarbor to make it more functional and engaging for designers on PixelHarbor.
* The page you are redesigning is here: http://www.pixelharbor-example.com/my-profile.
* Your design should allow for the same functionality as the existing page, though you don't need to replicate the same elements (buttons) or the same menu structure.
* Your design must fit with the branding of the site.
* You must provide a brief outline of what changes you made and why when you upload your design
* 1 submission per designer - make it your best work!
* Pls see "Must haves" for requirements.

Deadline:
* Submit before 12:00am 1st September UTC. Pls convert this deadline to your local timezone and take note of the local time and date

Prizes: $1,000 to win
* First prize for the best design is $700
* Second prize is $200
* Third prize is $100

If you started from scratch, how would you design the MyAccount page on PixelHarbor?

Good luck & have fun!

Mel / The PixelHarbor Team

Target Market(s)

PixelHarbor designers

Number of Pages Required

1 page

Requirements
Must have
• Dimensions: 1200 x 1000 px
• Minimum 150-300 dpi
• Your design must adhere to our quality standards to be eligible to receive a prize
• Submissions must be created in Adobe Creative Suite (Illustrator or Photoshop)
• Your design must fit with the branding of the PixelHarbor site.
• Only new registrants this month are eligible to enter and win prizes.

```html
<!DOCTYPE html>
<html lang="en">
<head>
<meta charset="utf-8">
<title>PixelHarbor – My Account Overview</title>
<link href="https://fonts.googleapis.com/css2?family=Open+Sans:wght@400;600;700&display=swap" rel="stylesheet">
<style>
:root{
  --ink:#333;
  --muted:#8a8a8a;
  --blue:#1f8fd6;
  --blue-dark:#1774b3;
  --green:#8cc63f;
  --dark:#2b2b2b;
  --darker:#222;
  --panel-head:#353535;
  --line:#dcdcdc;
  --page:#eeeeee;
  --white:#fff;
  --footer-text:#9a9a9a;
}
*{box-sizing:border-box;margin:0;padding:0}
html,body{width:874px;height:1200px;overflow:hidden}
body{font-family:"Open Sans",Arial,sans-serif;color:var(--ink);background:var(--page);font-size:11px;position:relative}
.topbar{height:62px;background:var(--dark);display:flex;align-items:center;padding:0 58px;gap:20px}
.brand{display:flex;align-items:center;gap:8px;color:var(--white);font-weight:700;font-size:20px}
.brand-dot{width:18px;height:18px;border-radius:50%;background:var(--blue)}
.main-nav{display:flex;gap:14px;color:#ddd;font-size:10.5px;font-weight:600}
.main-nav .phone{color:var(--muted)}
.flag-chip{width:14px;height:9px;background:#556;display:inline-block;vertical-align:middle;margin-left:4px}
.top-actions{margin-left:auto;display:flex;gap:8px;align-items:center}
.profile-select{width:104px;height:22px;background:var(--white);border-radius:2px;font-size:10px;padding:4px 8px;position:relative}
.profile-select:after{content:"▾";position:absolute;right:6px;top:3px;color:var(--muted)}
.btn-green{background:var(--green);color:var(--white);font-weight:600;font-size:10px;padding:5px 12px;border-radius:2px}
.crumbs{height:30px;background:#e2e2e2;border-bottom:1px solid var(--line);display:flex;align-items:center;padding:0 58px;gap:12px;font-size:10px;color:#666}
.page-title{text-align:center;color:var(--blue);font-size:27px;font-weight:600;margin:16px 0 4px}
.title-rule{width:56px;height:2px;background:var(--blue);margin:0 auto 14px}
.stats{margin:0 58px;height:70px;background:var(--white);border:1px solid var(--line);display:flex;align-items:center}
.avatar{width:70px;height:70px;background:var(--blue);display:flex;align-items:center;justify-content:center}
.stat{flex:1;text-align:center;border-right:1px solid var(--line)}
.stat:last-child{border-right:0}
.stat h4{color:var(--blue);font-size:12px;font-weight:700}
.stat .val{font-size:10px;font-weight:600}
.stat small{display:block;color:var(--muted);font-size:9px}
.content{display:flex;gap:16px;margin:34px 58px 0}
.side-nav{width:174px;background:var(--dark);align-self:flex-start}
.side-nav li{list-style:none;color:#ccc;font-size:10.5px;padding:11px 12px;border-bottom:1px solid #3c3c3c;position:relative}
.side-nav li:after{content:"›";position:absolute;right:10px;color:#777}
.side-nav li.active{background:var(--blue);color:var(--white)}
.col-main{flex:1;display:flex;flex-direction:column;gap:14px}
.panel{background:var(--white);border:1px solid var(--line)}
.panel-head{background:var(--panel-head);color:var(--white);font-weight:700;font-size:14px;padding:0 14px;height:52px;display:flex;align-items:center;justify-content:space-between}
.progress-ring{width:36px;height:36px}
.todo{padding:12px 16px 16px}
.todo h5{font-size:11px;margin-bottom:8px}
.todo li{list-style:none;display:flex;align-items:center;gap:10px;border-bottom:1px solid #eee;padding:7px 0;font-size:10px}
.todo li:before{content:"";width:8px;height:8px;border-radius:50%;background:#bbb}
.todo .state{margin-left:auto}
.done{background:#555;color:var(--white);font-size:8.5px;padding:2px 8px;border-radius:2px}
.tick{color:#333;font-weight:700}
.pair{display:flex;gap:14px}
.pair .panel{flex:1}
.pair .panel-head{height:34px;justify-content:center;font-size:12px}
.job{display:flex;gap:8px;padding:7px 10px;border-bottom:1px solid #eee}
.job-dot{width:14px;height:14px;border-radius:50%;border:2px solid #bcd;flex-shrink:0;margin-top:3px}
.job p{font-size:8.5px;font-weight:700}
.job .tags{display:flex;gap:4px;margin-top:3px}
.job .tags span{border:1px solid var(--line);font-size:7.5px;padding:1px 4px;color:#666}
.pager{display:flex;justify-content:space-between;padding:6px 10px;font-size:8.5px;color:#666}
.ach{display:flex;gap:8px;padding:8px 12px;align-items:center}
.ach-badge{width:18px;height:18px;border-radius:50%;background:#777}
.ach b{font-size:9px;display:block}
.ach span{font-size:8px;color:var(--muted)}
.footer{position:absolute;left:0;right:0;top:917px;bottom:0;background:var(--darker);padding:24px 58px 0;color:var(--footer-text)}
.foot-cols{display:flex;gap:26px}
.foot-col{width:104px}
.foot-col h6{color:var(--white);font-size:12px;margin-bottom:10px}
.foot-col li{list-style:none;font-size:8.5px;margin-bottom:7px}
.popular{width:150px}
.popular .tag{display:inline-block;border:1px solid #444;font-size:8px;padding:2px 5px;margin:0 3px 5px 0}
.subscribe{margin-left:auto;width:200px}
.subscribe h6{color:var(--white);font-size:10px;margin-bottom:8px;display:flex;gap:6px;align-items:center}
.sub-row{display:flex;gap:4px;margin-bottom:12px}
.sub-input{flex:1;height:22px;background:var(--white);border-radius:2px}
.sub-btn{background:var(--green);color:var(--white);font-size:9px;font-weight:700;padding:4px 8px;border-radius:2px}
.squares{display:flex;gap:6px;flex-wrap:wrap;width:120px;margin-bottom:14px}
.squares i{width:24px;height:24px;background:#4a4a4a;border-radius:3px}
.flags{display:flex;gap:6px}
.flags i{width:20px;height:13px;background:#555}
.foot-brand{color:var(--white);font-weight:700;font-size:15px;margin-top:12px;text-align:right}
.copyright{position:absolute;left:0;right:0;bottom:0;height:34px;border-top:1px solid #333;text-align:center;font-size:8px;padding-top:12px;color:#777}
</style>
</head>
<body>
<header class="topbar">
  <div class="brand"><span class="brand-dot"></span>PixelHarbor</div>
  <nav class="main-nav"><span>Categories</span><span>Designers</span><span>Browse jobs</span><span>How it works</span><span class="phone">1800 555 0142 <i class="flag-chip"></i></span></nav>
  <div class="top-actions"><div class="profile-select">My Profile</div><div class="btn-green">Become a buyer</div></div>
</header>
<div class="crumbs">
  <svg width="11" height="10" viewBox="0 0 11 10"><path d="M5.5 0 11 5H9v5H6.5V7h-2v3H2V5H0z" fill="#666"/></svg>
  <span>Home</span><span>›</span><span>My Profile</span>
</div>
<h1 class="page-title">Overview</h1>
<div class="title-rule"></div>
<section class="stats">
  <div class="avatar"><svg width="30" height="30" viewBox="0 0 30 30"><circle cx="15" cy="10" r="7" fill="#fff"/><path d="M2 30c0-8 6-12 13-12s13 4 13 12z" fill="#fff"/></svg></div>
  <div class="stat"><h4>Rank</h4><div class="val">4436/71</div><small>of 115,000 designers</small></div>
  <div class="stat"><h4>Positive</h4><div class="val">0%</div><small>(0%)</small></div>
  <div class="stat"><h4>Submissions</h4><div class="val">0</div><small>(on average 7)</small></div>
  <div class="stat"><h4>Earnings</h4><div class="val">$0</div><small>(on average $7,000 AU)</small></div>
</section>
<div class="content">
  <ul class="side-nav">
    <li class="active">Overview</li><li>Notifications</li><li>Invites</li><li>Submissions</li><li>Messages</li><li>Watchlist</li><li>Widgets</li><li>My Profile</li>
  </ul>
  <div class="col-main">
    <section class="panel">
      <div class="panel-head">Getting Started - Complete Your Profile
        <svg class="progress-ring" viewBox="0 0 36 36"><circle cx="18" cy="18" r="15" fill="none" stroke="#555" stroke-width="4"/><circle cx="18" cy="18" r="15" fill="none" stroke="#fff" stroke-width="4" stroke-dasharray="70.7 94.2" transform="rotate(-90 18 18)"/><text x="18" y="21" text-anchor="middle" font-size="8" fill="#fff" font-family="Open Sans,sans-serif" font-weight="700">75%</text></svg>
      </div>
      <div class="todo">
        <h5>Things left to do:</h5>
        <ul>
          <li>Tell us what type of designer you are<span class="state tick">✔</span></li>
          <li>Verify your payment address<span class="state tick">✔</span></li>
          <li>Visit the Jobs Board<span class="state tick">✔</span></li>
          <li>Add your profile pic<span class="state done">Completed</span></li>
          <li>Add an about me to your profile<span class="state tick">✔</span></li>
          <li>Review and accept the PixelHarbor quality standards<span class="state done">Completed</span></li>
          <li>Submit your first design<span class="state done">Completed</span></li>
        </ul>
      </div>
    </section>
    <div class="pair">
      <section class="panel">
        <div class="panel-head">Recommended Jobs</div>
        <div class="job"><i class="job-dot"></i><div><p>Lorem ipsum is simply dummy text of the Art</p><div class="tags"><span>5 Days Left</span><span>$ 300</span><span>Branding</span></div></div></div>
        <div class="job"><i class="job-dot"></i><div><p>Lorem ipsum is simply dummy text of the Web</p><div class="tags"><span>5 Days Left</span><span>$ 300</span><span>Branding</span></div></div></div>
        <div class="job"><i class="job-dot"></i><div><p>Lorem ipsum is simply dummy text of the Logo</p><div class="tags"><span>5 Days Left</span><span>$ 300</span><span>Branding</span></div></div></div>
        <div class="job"><i class="job-dot"></i><div><p>Lorem ipsum is simply dummy text of the Print</p><div class="tags"><span>5 Days Left</span><span>$ 300</span><span>Branding</span></div></div></div>
        <div class="pager"><span>Page 1</span><span>‹ ›</span></div>
      </section>
      <section class="panel">
        <div class="panel-head">Achievements</div>
        <div class="ach"><i class="ach-badge"></i><div><b>Rookie (Next)</b><span>Submit at least 1 design to contests</span></div></div>
        <div class="ach"><i class="ach-badge"></i><div><b>Rookie (Next)</b><span>Submit at least 1 design to contests</span></div></div>
        <div class="ach"><i class="ach-badge"></i><div><b>Rookie (Next)</b><span>Submit at least 1 design to contests</span></div></div>
      </section>
    </div>
  </div>
</div>
<footer class="footer">
  <div class="foot-cols">
    <div class="foot-col"><h6>I need a...</h6><ul><li>Logo design</li><li>Website design</li><li>Business card</li><li>Brochure design</li><li>Banner design</li><li>Book cover</li><li>T-shirt design</li></ul></div>
    <div class="foot-col"><h6>Find a...</h6><ul><li>Logo designer</li><li>Web designer</li><li>Graphic designer</li><li>Print designer</li><li>Freelancer</li><li>Illustrator</li><li>Copywriter</li></ul></div>
    <div class="foot-col"><h6>About us</h6><ul><li>Our story</li><li>Press room</li><li>Careers</li><li>Affiliate program</li><li>Contact us</li><li>Terms of use</li><li>Privacy policy</li></ul></div>
    <div class="foot-col popular"><h6>Popular pages</h6>
      <span class="tag">Logo contests</span><span class="tag">Web design</span><span class="tag">Print</span><span class="tag">Business cards</span><span class="tag">Packaging</span><span class="tag">Icons</span><span class="tag">Book cover</span><span class="tag">Apparel</span><span class="tag">Flyers</span><span class="tag">Banners</span>
    </div>
    <div class="subscribe">
      <h6><svg width="12" height="9" viewBox="0 0 12 9"><rect width="12" height="9" fill="#888"/><path d="M0 0l6 5 6-5" fill="none" stroke="#222"/></svg>Subscribe to our newsletter</h6>
      <div class="sub-row"><div class="sub-input"></div><div class="sub-btn">JOIN</div></div>
      <div class="squares"><i></i><i></i><i></i><i></i><i></i><i></i><i></i><i></i></div>
      <div class="flags"><i></i><i></i><i></i><i></i><i></i></div>
      <div class="foot-brand">PixelHarbor</div>
    </div>
  </div>
  <div class="copyright">Copyright © 2013 PixelHarbor Pty Ltd. All rights reserved. Terms of Use · Privacy Policy</div>
</footer>
</body>
</html>
```